Designing a brochures for an educational counseling service provider

We would like a 4 sided design on a 11x8.5 paper, half folded. I have including a sample design we did to give you an idea of what we envision but we welcome creativity to make beautiful looking flyers. Text for the flier is included as well as our logo.
- The most important thing is capturing our audience/market. We will be handing these flies to schools, organizations and individual clients.

www.vormtaleducationalconsultants.com

Target Market(s)

We are targeting international students wanting to study in the U.S and Canada.

Industry/Entity Type

Education

Requirements
Must have
• - Clean and clear
• - Our logo should visible and well placed.
• - Could you the pictures of students, libraries and school buildings or you could use the pictures we already have.
Nice to have
• We would like this to match business cards.

```html
<!DOCTYPE html>
<html lang="en">
<head>
<meta charset="utf-8">
<title>Vormtal Educational Consultants – Brochure</title>
<link rel="stylesheet" href="https://fonts.googleapis.com/css2?family=Montserrat:ital,wght@0,800;0,900;1,800&family=Titillium+Web:wght@700&family=Source+Sans+3:wght@400;600&display=swap">
<style>
  :root{
    --orange:#ef5a24;
    --charcoal:#3b3d40;
    --ink:#2a2a2a;
    --text:#333;
    --white:#fff;
    --navy:#1e3a78;
  }
  html,body{margin:0;padding:0;background:#fff;overflow:hidden;}
  .canvas{position:relative;width:781px;height:1200px;overflow:hidden;background:#fff;font-family:"Source Sans 3",sans-serif;color:var(--text);}
  .abs{position:absolute;}
  .cover-art{position:absolute;left:0;top:0;}
  .tagline{position:absolute;left:580px;top:259px;transform:translate(-50%,-50%) rotate(-10.1deg);white-space:nowrap;
    font-family:"Montserrat",sans-serif;font-weight:800;font-style:italic;font-size:8.6px;color:var(--white);letter-spacing:.2px;}
  .brand{position:absolute;left:478px;top:118px;display:flex;align-items:center;gap:10px;}
  .brand-dot{width:34px;height:34px;border-radius:50%;background:var(--navy);}
  .brand-name{font-family:"Titillium Web",sans-serif;font-weight:700;font-size:15px;line-height:16px;color:var(--navy);}
  .service-list{position:absolute;left:481px;top:330px;margin:0;padding:0;list-style:none;}
  .service-list li{display:flex;align-items:center;height:42px;margin-bottom:7.6px;}
  .service-list svg{width:42px;height:42px;color:var(--white);flex:none;}
  .service-list span{margin-left:10px;font-family:"Titillium Web",sans-serif;font-weight:700;font-size:18px;color:var(--white);letter-spacing:.3px;}
  .cover-contact{position:absolute;left:129px;top:512px;font-size:7.1px;line-height:9.2px;color:var(--white);}
  .cover-contact b{font-weight:600;}
  .phone-tile{position:absolute;left:74px;top:516px;width:37px;height:37px;color:var(--white);}
  .footer-bar{position:absolute;left:10px;top:564px;width:760px;height:31px;background:var(--charcoal);}
  .footer-bar p{margin:0;position:absolute;right:5px;top:9px;font-size:8.2px;color:#e8e8e8;}
  .spine{position:absolute;width:4px;background:var(--orange);}
  .dot{position:absolute;width:20px;height:20px;border-radius:50%;background:var(--orange);transform:translate(-50%,-50%);}
  .banner{position:absolute;left:10px;width:386px;}
  .h-section{position:absolute;margin:0;font-family:"Montserrat",sans-serif;font-weight:900;letter-spacing:.3px;white-space:nowrap;}
  .h-light{color:var(--white);}
  .h-dark{color:var(--ink);}
  .body{position:absolute;margin:0;font-size:10.3px;line-height:12.3px;text-align:justify;}
  .body p{margin:0 0 12.3px;}
  .body p:last-child{margin-bottom:0;}
  .on-dark{color:var(--white);}
  .pkg{margin:0;padding:0;list-style:none;}
  .pkg li{padding-left:0;}
  .pkg li::before{content:">";display:inline-block;width:35px;}
  .card{position:absolute;left:432px;width:338px;background:var(--orange);border-radius:6px;}
</style>
</head>
<body>
<div class="canvas">

  <svg width="0" height="0" style="position:absolute" aria-hidden="true">
    <defs>
      <symbol id="i-frame" viewBox="0 0 100 100"><rect x="6" y="6" width="88" height="88" rx="22" fill="none" stroke="currentColor" stroke-width="8"/></symbol>
      <symbol id="i-up" viewBox="0 0 100 100"><use href="#i-frame"/><polyline points="27,62 50,38 73,62" fill="none" stroke="currentColor" stroke-width="9" stroke-linecap="round" stroke-linejoin="round"/></symbol>
      <symbol id="i-pen" viewBox="0 0 100 100"><use href="#i-frame"/><path d="M28 72 L33 57 L61 29 L71 39 L43 67 Z" fill="currentColor"/></symbol>
      <symbol id="i-swap" viewBox="0 0 100 100"><use href="#i-frame"/><circle cx="38" cy="35" r="8" fill="currentColor"/><path d="M24 57 q14 -16 28 0 v3 h-28z" fill="currentColor"/><circle cx="62" cy="54" r="8" fill="currentColor"/><path d="M48 77 q14 -16 28 0 v3 h-28z" fill="currentColor"/><path d="M56 28 q12 2 14 14" fill="none" stroke="currentColor" stroke-width="3.5"/><path d="M28 64 q2 12 14 14" fill="none" stroke="currentColor" stroke-width="3.5"/></symbol>
      <symbol id="i-cap" viewBox="0 0 100 100"><use href="#i-frame"/><polygon points="50,32 82,45 50,58 18,45" fill="currentColor"/><path d="M33 52 v12 q17 9 34 0 v-12 l-17 7z" fill="currentColor"/></symbol>
      <symbol id="i-phone" viewBox="0 0 100 100"><use href="#i-frame"/><path d="M36 26 l9 0 l4 14 l-7 5 q6 12 15 16 l5 -7 l14 4 l0 9 q-2 7 -10 7 q-22 -2 -34 -27 q-4 -13 4 -21z" fill="none" stroke="currentColor" stroke-width="5" stroke-linejoin="round"/></symbol>
      <linearGradient id="g-cover" x1="0" y1="0" x2="1" y2="1"><stop offset="0" stop-color="#c9c9c9"/><stop offset=".5" stop-color="#a9a9a9"/><stop offset="1" stop-color="#d8d8d8"/></linearGradient>
    </defs>
  </svg>

  <!-- Cover -->
  <svg class="cover-art" width="781" height="600" viewBox="0 0 781 600">
    <rect x="10" y="5" width="760" height="560" fill="var(--orange)"/>
    <polygon points="390,5 770,5 770,200 390,268" fill="#fff"/>
    <polygon points="390,268 770,200 770,244 390,312" fill="var(--charcoal)"/>
    <polygon points="10,5 390,5 390,452 10,500" fill="url(#g-cover)" role="img" aria-label="Black and white photo of a group of smiling students"/>
    <g color="var(--orange)">
      <use href="#i-up" x="112" y="164" width="82" height="82"/>
      <use href="#i-pen" x="208" y="164" width="82" height="82"/>
      <use href="#i-swap" x="112" y="264" width="82" height="82"/>
      <use href="#i-cap" x="208" y="264" width="82" height="82"/>
    </g>
  </svg>

  <div class="brand"><div class="brand-dot"></div><div class="brand-name">Vormtal Educational<br>Consultants</div></div>
  <div class="tagline">QUALITY EDUCATION ACCESSIBLE AND AFFORDABLE ACCROSS THE GLOBE.</div>

  <ul class="service-list">
    <li><svg viewBox="0 0 100 100"><use href="#i-up"/></svg><span>Boarding Schools</span></li>
    <li><svg viewBox="0 0 100 100"><use href="#i-pen"/></svg><span>College Admissions</span></li>
    <li><svg viewBox="0 0 100 100"><use href="#i-swap"/></svg><span>Transfer Students</span></li>
    <li><svg viewBox="0 0 100 100"><use href="#i-cap"/></svg><span>Graduate Students</span></li>
  </ul>

  <svg class="phone-tile" viewBox="0 0 100 100"><use href="#i-phone"/></svg>
  <div class="cover-contact">
    <b>Executive Director &amp; Independent Educational Consultant</b><br>
    <b>Vormtal Educational Consultants, LLC</b><br>
    1180 Alder Road<br>
    Suite 310, Fairhaven, TX, 75011<br>
    Phone No. : 555-210-3840
  </div>

  <div class="footer-bar"><p>Fairhaven, Texas &nbsp;|&nbsp; +1-555-210-3840 &nbsp;|&nbsp; info@vormtaleducationalconsultants.com</p></div>

  <!-- Inside left -->
  <div class="spine" style="left:23px;top:605px;height:595px;"></div>
  <div class="spine" style="left:413px;top:605px;height:595px;"></div>

  <div class="banner" role="img" aria-label="Photo of students studying together in a library" style="top:606px;height:84px;background:linear-gradient(90deg,#2a2224 0%,#5a4238 45%,#8a6448 75%,#3a2c28 100%);"></div>
  <div class="dot" style="left:25px;top:668px;"></div>
  <h2 class="h-section h-light" style="left:43px;top:650px;font-size:30px;">ABOUT US</h2>

  <div class="body" style="left:46px;top:714px;width:330px;">
    <p>Our mission is to make quality education accessible and affordable to the families we serve. Our services are designed with the child's future in mind. Whether one is seeking an academic or non-academic environment, it is important to us that we set our clients up for success.</p>
    <p>We are a family-centered organization and our goals are the same as those of our clients; for their child to thrive and reach their goals and dreams. With over 10 years of experience in the business, we are aware of the financial obstacles created by the ever increasing cost in education. Our expert consultants work closely with families to map out their educational budget and find the best affordable and quality educational options.</p>
  </div>

  <div class="banner" role="img" aria-label="Photo of library bookshelves" style="top:876px;height:230px;background:linear-gradient(110deg,#1c1d22 0%,#3a3c44 40%,#6a6e78 70%,#2a2b30 100%);"></div>
  <div class="dot" style="left:25px;top:902px;"></div>
  <h2 class="h-section h-light" style="left:46px;top:884px;font-size:28px;">SERVICES</h2>
  <div class="body on-dark" style="left:46px;top:927px;width:330px;">
    <p>Finding the right school or program for your child is one of the most important decisions your family will make. The right choice will make a major impact on your child's future.</p>
    <p>Our package includes:</p>
    <ul class="pkg" style="text-align:left;">
      <li>Intake interview</li>
      <li>Present range of options based on needs and goals of the family</li>
      <li>Interview coaching</li>
      <li>Assistance with application and essays</li>
      <li>Updates on student progress throughout their enrollment with the school,</li>
      <li>Advisement on financial documents and visa applications</li>
    </ul>
  </div>

  <div class="dot" style="left:25px;top:1126px;"></div>
  <h2 class="h-section h-dark" style="left:46px;top:1108px;font-size:28px;">BOARDING SCHOOLS</h2>
  <div class="body" style="left:46px;top:1150px;width:330px;">
    <p>Students who want the best out of their grade school experience are likely to choose boarding schools because they are proven to better prepare students for university. North American boarding schools</p>
  </div>

  <!-- Inside right -->
  <div class="body" style="left:437px;top:605px;width:329px;">
    <p>provide a quality dynamic experience that will facilitate personal growth in independence, leadership, and confidence as well as provide the academic curriculum necessary to prepare students for university.</p>
  </div>

  <div class="card" style="top:653px;height:211px;"></div>
  <div class="dot" style="left:415px;top:674px;"></div>
  <h2 class="h-section h-light" style="left:437px;top:656px;font-size:28.5px;">COLLEGE ADMISSION</h2>
  <div class="body on-dark" style="left:437px;top:696px;width:329px;">
    <p>As Educational Consultants, we specialize in college/university admissions and we understand how confusing, time-consuming, and stressful the application process can be. Our experienced counselors are here to answer your questions and guide you step by step. As Parents and students may have limited access to information on schools, may not know or understand the entire process as a whole, nor where/how to begin, our experts counselors have a solutions.</p>
    <p>Clients increase the odds of admissions with our comprehensive plan of action. We believe that regardless of a student's level of involvement in extra-curricular activities or preparedness, they still possess something they can offer to the university; therefore we help them shine on their college applications.</p>
  </div>

  <div class="dot" style="left:415px;top:890px;"></div>
  <h2 class="h-section h-dark" style="left:437px;top:880px;font-size:28px;">TRANSFER STUDENTS</h2>
  <div class="body" style="left:437px;top:921px;width:329px;">
    <p>Need to find a school an alternative school that is a better match for you? We work with students and families to transfer from one school to another.</p>
  </div>

  <div class="card" style="top:968px;height:216px;"></div>
  <div class="dot" style="left:415px;top:981px;"></div>
  <h2 class="h-section h-light" style="left:437px;top:972px;font-size:28.5px;">SCHOLARSHIPS</h2>
  <div class="body on-dark" style="left:437px;top:1013px;width:329px;">
    <p>Funding the education for your children in some of the world's top schools can be very expensive as tuition and fees increase at an average of 4% every year. We work with you to determine the budget for your family, applying to scholarship available and guide you through the financial aid process.</p>
    <p>Over 70% of our clients have been awarded scholarships or Financial Aid, making your education goals attainable an affordable and your children education possible.</p>
    <p>Include at the bottom of last page "Our consultants are members of ACEC, the leading association for educational consultants in North America."</p>
  </div>

</div>
</body>
</html>
```